Plakate für Haushaltshilfen und Alltagsbegleiter
Zielgruppe
Wir bieten haushaltsnahe Dienstleistungen (Haushaltshilfen und Altgasbegleiter) für Personen mit einem Pflegegrad 1 - 5 an.
Zielgruppe sind Personen mit einem Pflegegrad 1 - 5. Hauptsächlich ältere Menschen die Unterstützung/Betreuung im Alltag und Haushalt benötigen.
Aufgabenstellung
Wir benötigen für unsere Büroräume eine Fensterbeschriftung. Es handelt sich hier um 5 Fenster (Glasflächen) und eine Glastür. Die Vorgabe ist, dass von außen zu erkennen ist dass sich um alle Räumlichkeiten um unsere (Firma Lindwerk) Räumlichkeiten handelt. Desweiteren soll auch unser Angebot erkennbar sein.
Unser Angebot enthält: Haushaltshilfen und Alltagsbegleiter
- kostenlose Haushaltshilfe ab Pflegegrad 1
- Abrechnung mit allen Kostenträgern
Da wir keine Schilder an die Fassade anbringen können, müßen die Glasflächen dafür genutzt werden um zum Einen uns als Firma erkennbar zu machen und zum anderen unser Angebot kurz zu präsentieren.
Uns ist wichtig dass unser Logo verwendet wir und auch unsere Farben.
Desweiteren sollten an den Fenstern auch teilweise eine Sichtschutz nach innen, angebracht werden, aber eben nur teilweise also nicht das ganzen Fenster z.Bsp. mit einer Blickdichten Folie überziehen, sondern in Augenhöhe wenn Fußgänger vorbei laufen.

```html
<!DOCTYPE html>
<html lang="de">
<head>
<meta charset="utf-8">
<title>Lindwerk – Fensterbeschriftung</title>
<link href="https://fonts.googleapis.com/css2?family=Montserrat:wght@400;600;700;800&display=swap" rel="stylesheet">
<style>
  :root {
    --red: #d8232a;
    --red-dark: #a8161c;
    --ink: #2b2b2d;
    --ink-deep: #1c1c1e;
    --white: #ffffff;
    --paper: #eeeeec;
    --grey-soft: #c9c9c9;
    --backdrop: #e4e2dd;
  }
  * { box-sizing: border-box; margin: 0; padding: 0; }
  html, body { width: 1200px; height: 590px; overflow: hidden; }
  body {
    background: var(--backdrop);
    font-family: "Montserrat", Arial, sans-serif;
    color: var(--ink);
  }
  .facade {
    position: relative;
    width: 1200px; height: 590px;
    display: flex; gap: 20px;
    justify-content: center; align-items: flex-start;
    padding-top: 112px;
  }
  .panel {
    position: relative;
    width: 180px; height: 255px;
    overflow: hidden;
    background: var(--white);
    box-shadow: 0 2px 8px rgba(0,0,0,.15);
  }
  .panel--door { width: 165px; height: 365px; background: var(--ink-deep); }
  .panel--dark { background: var(--ink); }
  .shape { position: absolute; inset: 0; width: 100%; height: 100%; }
  .photo { position: absolute; left: 0; right: 0; }

  .brand {
    position: absolute; left: 0; right: 0;
    display: flex; align-items: center; justify-content: center; gap: 5px;
  }
  .brand__dot { width: 11px; height: 11px; border-radius: 50%; background: var(--red); flex: none; }
  .brand__name { font-weight: 700; font-size: 11px; letter-spacing: .5px; text-transform: uppercase; color: var(--ink); }
  .brand--light .brand__dot { background: var(--white); }
  .brand--light .brand__name { color: var(--white); }
  .brand__tag {
    position: absolute; left: 0; right: 0; text-align: center;
    font-size: 4.5px; letter-spacing: .6px; text-transform: uppercase; color: var(--ink);
  }
  .brand__tag--light { color: var(--white); }

  /* Vorteile */
  .benefits__bar {
    position: absolute; top: 66px; left: 6px; right: 6px; height: 14px;
    background: var(--ink); color: var(--white);
    font-size: 8px; font-weight: 700; text-align: center; line-height: 14px;
  }
  .benefits__grid {
    position: absolute; top: 88px; left: 12px; right: 12px;
    display: grid; grid-template-columns: 1fr 1fr; gap: 10px 10px;
  }
  .benefit { text-align: center; }
  .benefit__icon {
    width: 22px; height: 22px; margin: 0 auto 4px; border-radius: 3px;
    background: var(--red); display: flex; align-items: center; justify-content: center;
  }
  .benefit__text { font-size: 5px; line-height: 1.35; color: #555; }

  .claim {
    position: absolute; left: 8px; right: 8px; text-align: center;
    font-size: 7px; font-weight: 700; line-height: 1.35; color: var(--white); text-transform: uppercase;
  }
  .headline {
    position: absolute; left: 8px; right: 8px; text-align: center;
    font-size: 9.5px; font-weight: 800; line-height: 1.25; color: var(--red); text-transform: uppercase;
  }
  .tag {
    position: absolute; background: var(--red); color: var(--white);
    font-size: 5.5px; font-weight: 700; line-height: 1.25; text-transform: uppercase; text-align: center;
    padding: 3px 6px; border-radius: 3px; transform: rotate(-8deg);
  }
  .door__copy {
    position: absolute; top: 104px; left: 14px; right: 14px; text-align: right;
    font-size: 7px; font-weight: 700; line-height: 1.4; color: var(--white); text-transform: uppercase;
  }
  .contact { position: absolute; left: 0; right: 0; bottom: 14px; text-align: center; color: var(--white); }
  .contact__lead { font-size: 6.5px; margin-bottom: 5px; }
  .contact__phone {
    display: inline-block; background: var(--red); border-radius: 3px;
    font-size: 10px; font-weight: 800; padding: 2px 8px; margin-bottom: 8px;
  }
  .contact__web { font-size: 8px; font-weight: 600; }
</style>
</head>
<body>
<main class="facade">

  <!-- Fenster 1: Vorteile -->
  <section class="panel panel--benefits">
    <svg class="shape" viewBox="0 0 180 255" preserveAspectRatio="none" aria-hidden="true">
      <polygon points="0,215 90,250 180,200 180,255 0,255" fill="var(--ink)"/>
      <polygon points="0,215 90,250 180,200 180,228 100,255 0,255" fill="var(--red)"/>
    </svg>
    <div class="brand" style="top:26px"><span class="brand__dot"></span><span class="brand__name">Lindwerk</span></div>
    <div class="brand__tag" style="top:44px">Haushaltshilfen &amp; Mehr</div>
    <div class="benefits__bar">UNSERE VORTEILE</div>
    <div class="benefits__grid">
      <div class="benefit">
        <div class="benefit__icon"><svg width="12" height="12" viewBox="0 0 12 12"><rect x="2.5" y="1" width="7" height="10" rx="1" fill="none" stroke="#fff" stroke-width="1.2"/><path d="M4 4h4M4 6h4M4 8h2" stroke="#fff" stroke-width="1"/></svg></div>
        <p class="benefit__text">Abrechnung mit allen Pflegekassen möglich</p>
      </div>
      <div class="benefit">
        <div class="benefit__icon"><svg width="12" height="12" viewBox="0 0 12 12"><path d="M6 1v6M3.5 4.5 6 7l2.5-2.5" fill="none" stroke="#fff" stroke-width="1.3"/><path d="M1.5 9h9" stroke="#fff" stroke-width="1.3"/></svg></div>
        <p class="benefit__text">Abrechnung über den Entlastungsbetrag möglich</p>
      </div>
      <div class="benefit">
        <div class="benefit__icon"><svg width="12" height="12" viewBox="0 0 12 12"><path d="M6 10.5 1.8 6.3A2.4 2.4 0 0 1 6 3a2.4 2.4 0 0 1 4.2 3.3Z" fill="#fff"/></svg></div>
        <p class="benefit__text">Auch über die Verhinderungspflege</p>
      </div>
      <div class="benefit">
        <div class="benefit__icon"><svg width="12" height="12" viewBox="0 0 12 12"><rect x="1.5" y="2" width="7" height="9" rx="1" fill="none" stroke="#fff" stroke-width="1.1"/><path d="m5 8 5.5-5.5" stroke="#fff" stroke-width="1.4"/></svg></div>
        <p class="benefit__text">Hilfe bei der Antragstellung</p>
      </div>
    </div>
  </section>

  <!-- Fenster 2: Angebot -->
  <section class="panel panel--offer">
    <div class="photo" style="top:0;height:185px;background:linear-gradient(160deg,#f3f1ee 0%,#d9cfc8 55%,#8d8480 100%)" role="img" aria-label="Foto eines lachenden älteren Paares"></div>
    <div class="brand" style="top:22px"><span class="brand__dot"></span><span class="brand__name">Lindwerk</span></div>
    <svg class="shape" viewBox="0 0 180 255" preserveAspectRatio="none" aria-hidden="true">
      <polygon points="0,170 60,182 120,166 180,150 180,255 0,255" fill="var(--ink)"/>
      <polygon points="0,170 60,182 180,150 180,172 70,192 0,182" fill="var(--red)"/>
    </svg>
    <p class="claim" style="top:205px">Wir bieten Haushaltshilfen und Alltagsbegleiter für Privathaushalte an.</p>
  </section>

  <!-- Fenster 3: Headline -->
  <section class="panel panel--headline">
    <div class="photo" style="top:115px;height:140px;background:linear-gradient(135deg,#cfd9e6 0%,#eae6e1 50%,#b9b4ad 100%)" role="img" aria-label="Foto einer Familie mit älterem Mann"></div>
    <svg class="shape" viewBox="0 0 180 255" preserveAspectRatio="none" aria-hidden="true">
      <polygon points="0,0 180,0 180,16 0,56" fill="var(--ink)"/>
      <polygon points="0,0 150,0 0,56" fill="var(--red)"/>
    </svg>
    <div class="brand" style="top:63px"><span class="brand__dot"></span><span class="brand__name">Lindwerk</span></div>
    <p class="headline" style="top:83px">Haushaltshilfen und<br>Alltagsbegleiter</p>
    <div class="tag" style="left:92px;top:212px">Kostenlose<br>Haushaltshilfe<br>ab Pflegegrad 1</div>
  </section>

  <!-- Fenster 4: Kostenträger -->
  <section class="panel panel--dark">
    <div class="photo" style="top:110px;height:145px;background:linear-gradient(160deg,#e8e8e8 0%,#a9a9a9 55%,#3a3a3a 100%)" role="img" aria-label="Schwarzweißfoto: Hände eines älteren Menschen auf einem Gehstock"></div>
    <svg class="shape" viewBox="0 0 180 255" preserveAspectRatio="none" aria-hidden="true">
      <polygon points="0,75 60,90 120,78 180,60 180,112 0,112" fill="var(--ink)"/>
      <polygon points="0,75 60,90 180,60 180,78 70,102 0,92" fill="var(--red)"/>
    </svg>
    <div class="brand brand--light" style="top:24px"><span class="brand__dot"></span><span class="brand__name">Lindwerk</span></div>
    <div class="brand__tag brand__tag--light" style="top:40px">Haushaltshilfen &amp; Mehr</div>
    <div class="tag" style="left:88px;top:148px">Abrechnung mit<br>allen<br>Kostenträgern</div>
  </section>

  <!-- Glastür -->
  <section class="panel panel--door">
    <svg class="shape" viewBox="0 0 165 365" preserveAspectRatio="none" aria-hidden="true">
      <polygon points="0,0 120,0 0,70" fill="var(--red)"/>
      <polygon points="0,312 60,328 120,312 165,300 165,365 0,365" fill="var(--white)"/>
      <polygon points="0,305 60,322 165,294 165,315 70,338 0,322" fill="var(--red)"/>
    </svg>
    <div class="brand brand--light" style="top:64px"><span class="brand__dot"></span><span class="brand__name">Lindwerk</span></div>
    <div class="brand__tag brand__tag--light" style="top:80px">Haushaltshilfen &amp; Mehr</div>
    <p class="door__copy">Den Alltag zu bewältigen kann eine echte Herausforderung sein. Egal ob Sie Hilfe beim Einkaufen oder anderen alltäglichen Aktivitäten benötigen, wir helfen gerne.</p>
  </section>

  <!-- Fenster 5: Kontakt -->
  <section class="panel panel--dark">
    <div class="photo" style="top:0;height:150px;background:linear-gradient(160deg,#f2f2f2 0%,#d6d6d6 60%,#9a9a9a 100%)" role="img" aria-label="Foto: offene Hände halten eine kleine Familienfigur"></div>
    <svg class="shape" viewBox="0 0 180 255" preserveAspectRatio="none" aria-hidden="true">
      <polygon points="0,140 60,128 120,140 180,125 180,160 0,160" fill="var(--ink)"/>
      <polygon points="0,140 60,128 180,142 180,160 110,150 0,160" fill="var(--red)"/>
    </svg>
    <div class="contact">
      <p class="contact__lead">Buchen Sie gleich einen Termin:</p>
      <p class="contact__phone">0711 20 48 36 15</p>
      <p class="contact__web">www.lindwerk.de</p>
    </div>
  </section>

</main>
</body>
</html>
```